Modern, Sleek Business Card Design for Corvane Systems

Please create a modern business card, preferably all black with white logo and writing for Corvane Systems, a defense and aerospace company.

Contact Information for Business Card

symbol on one side and name, title, contact info on the other side.

```html
<!DOCTYPE html>
<html lang="en">
<head>
<meta charset="utf-8">
<title>Corvane Systems Business Card</title>
<link href="https://fonts.googleapis.com/css2?family=Montserrat:wght@400;500;700&display=swap" rel="stylesheet">
<style>
  :root {
    --backdrop: #4a4a4a;
    --card: #161616;
    --edge: #ffffff;
    --ink: #ffffff;
    --ink-soft: #e6e6e6;
    --mark-grey: #9a9a9a;
  }
  * { box-sizing: border-box; margin: 0; padding: 0; }
  html, body { width: 1200px; height: 801px; overflow: hidden; }
  body {
    background: var(--backdrop);
    font-family: "Montserrat", Arial, sans-serif;
    display: flex;
    align-items: center;
    justify-content: center;
    gap: 44px;
  }
  .card {
    width: 540px;
    height: 309px;
    background: var(--card);
    border: 2px solid var(--edge);
    position: relative;
    color: var(--ink);
  }
  /* Front: identity + contact */
  .card-front { display: flex; align-items: center; }
  .brand-block {
    width: 270px;
    display: flex;
    align-items: center;
    justify-content: center;
    gap: 10px;
  }
  .brand-dot { width: 14px; height: 14px; background: var(--ink); }
  .brand-name {
    font-weight: 500;
    font-size: 19px;
    letter-spacing: 2px;
    color: var(--ink);
    white-space: nowrap;
  }
  .divider {
    width: 1.5px;
    height: 150px;
    background: var(--ink);
  }
  .contact-block { padding-left: 26px; }
  .person-name {
    font-weight: 700;
    font-size: 21px;
    letter-spacing: 0.5px;
    text-transform: uppercase;
  }
  .person-title { font-size: 12.5px; color: var(--ink-soft); margin-top: 2px; }
  .address { font-size: 12.5px; color: var(--ink-soft); margin-top: 12px; line-height: 1.45; }
  .contact-list { list-style: none; margin-top: 8px; }
  .contact-list li {
    display: flex; align-items: center; gap: 7px;
    font-size: 12.5px; color: var(--ink-soft); line-height: 1.75;
  }
  .contact-list svg { width: 11px; height: 11px; fill: var(--ink); flex: none; }

  /* Back: name mark */
  .card-back { display: flex; align-items: center; justify-content: center; }
  .mark {
    text-align: center;
    color: var(--mark-grey);
    font-weight: 500;
  }
  .mark-main { font-size: 52px; letter-spacing: 4px; line-height: 1; }
  .mark-sub { font-size: 18px; letter-spacing: 12px; margin-top: 10px; padding-left: 12px; }
</style>
</head>
<body>
  <section class="card card-front">
    <div class="brand-block">
      <span class="brand-dot"></span>
      <span class="brand-name">CORVANE SYSTEMS</span>
    </div>
    <div class="divider"></div>
    <div class="contact-block">
      <h1 class="person-name">Elias Marlow</h1>
      <p class="person-title">Managing Director</p>
      <p class="address">Your address, City<br>State, Zip 1234</p>
      <ul class="contact-list">
        <li>
          <svg viewBox="0 0 24 24"><path d="M6.6 10.8a15 15 0 0 0 6.6 6.6l2.2-2.2c.3-.3.7-.4 1-.2 1.1.4 2.3.6 3.6.6.6 0 1 .4 1 1V20c0 .6-.4 1-1 1A17 17 0 0 1 3 4c0-.6.4-1 1-1h3.5c.6 0 1 .4 1 1 0 1.3.2 2.5.6 3.6.1.3 0 .7-.2 1z"/></svg>
          123 456 789
        </li>
        <li>
          <svg viewBox="0 0 24 24"><path d="M2 5h20v14H2zM4 7v.5l8 5 8-5V7l-8 5z"/></svg>
          info@youremail.com
        </li>
        <li>
          <svg viewBox="0 0 24 24"><circle cx="12" cy="12" r="10"/></svg>
          www.yourwebsite.com
        </li>
      </ul>
    </div>
  </section>

  <section class="card card-back">
    <div class="mark">
      <div class="mark-main">CORVANE</div>
      <div class="mark-sub">SYSTEMS</div>
    </div>
  </section>
</body>
</html>
```